Top notch designer needed for world class recruitment app!

We need an app design for an Amsterdam-based company that is about to change the way we find new jobs. The idea is not to show the company and job title as everyone does, but only a 5 sentence summary of the job. The user slides though the jobs and eventuelly finds a shortlist of his best matching jobs.

Winning designers supplies 2 designs, that have contain the core of our business idea (see screenshots attached):

Screenshot 1, A job description done in 5 bulletpoints (6-9 words).

example:

- Lead 20 enthusiastic workers
- Coordinate between production department and development team
- Improve current processes
- Maintain relations with supplier
- Lot of focus on personal development

Screenshot 2 should be a shortlist/favourites

The shortlists shows around 5 jobs with job title, company logo, number of days the
vacancy will stay available, and how well the job matches to your profile (preferably by means of a visual indicator).

Target Market(s)

Young professionals looking for a job. Well educated withless than 10 years work experience. Typical user would be someone who uses staffwell regularly.

Industry/Entity Type

Business

Requirements
Must have
• The 2 screenshots (see attachment) with awesome look and feel, with content as described in attachment.. The winning designs should (also) be available in PSD format, or less preferably in PNG.

Nice to have
• Inspiration:
Swoopa: simple and clear slide throughs (yes/no)
Staffwell: start screen (professional and stylish), vacancy banner (visual, but not distracting)
Roomvex: combination of playfull and professional design
Should not have
• We like to have it as visual as possible, but visuals cannot directly relate to the job (because we cannot match a visual to every job). So should be something 'business like' or 'city life'.

When a user clicks on the 'i (more info)' button the user can see info like job title, company name, location. Its important that this info is not shown in screenshot 1.

```html
<!DOCTYPE html>
<html lang="en">
<head>
<meta charset="utf-8">
<title>Job App – Shortlist & Job Description</title>
<link href="https://fonts.googleapis.com/css2?family=Roboto:wght@300;400;500&display=swap" rel="stylesheet">
<style>
:root{
  --canvas:#a6abb1;
  --shadow:#8b9096;
  --blue:#1584e3;
  --blue-top:#1a8cec;
  --ring:#1e9bf0;
  --track:#c8cbcf;
  --list-bg:#e9eaec;
  --card:#ffffff;
  --ink:#2e2e2e;
  --muted:#9a9a9a;
  --faint:#b0b0b0;
  --rule:#cfcfcf;
  --tick:#e02626;
  --red:#d81e1e;
  --navy:#1d3b7a;
  --white:#ffffff;
}
*{box-sizing:border-box;margin:0;padding:0}
html,body{width:1200px;height:1000px;overflow:hidden}
body{background:var(--canvas);font-family:"Roboto",Arial,sans-serif;position:relative}
.long-shadows{position:absolute;left:0;top:0}
.screen-title{position:absolute;top:30px;width:480px;text-align:center;color:var(--white);font-weight:300;font-size:40px;letter-spacing:-.3px}
.phone{position:absolute;top:119px;width:480px;height:851px;overflow:hidden;background:var(--list-bg)}
.phone--shortlist{left:106px}
.phone--detail{left:619px}
.screen-title--shortlist{left:106px}
.screen-title--detail{left:619px}

.status-bar{height:27px;background:var(--blue-top);color:var(--white);font-size:17px;display:flex;align-items:center;padding:0 10px;position:relative}
.status-bar .carrier{display:flex;align-items:center;gap:5px}
.status-bar .signal{font-size:11px;letter-spacing:1px}
.status-bar .time{position:absolute;left:0;right:0;text-align:center;pointer-events:none}
.status-bar .battery{margin-left:auto;display:flex;align-items:center;gap:6px}
.nav-bar{height:68px;background:var(--blue);display:flex;align-items:center;justify-content:space-between;padding:0 15px;color:var(--white)}
.nav-bar h1{font-weight:400;font-size:25px}

.job-list{padding:15px 15px 0}
.job-card{position:relative;height:105px;background:var(--card);margin-bottom:15px;box-shadow:0 1px 2px rgba(0,0,0,.12)}
.job-card .title{position:absolute;left:10px;top:9px;font-size:19px;color:var(--ink)}
.job-card .days{position:absolute;left:10px;top:35px;font-size:15px;color:var(--muted)}
.company{position:absolute;left:10px;top:68px;display:flex;align-items:center;gap:7px;font-size:16px;font-weight:500;letter-spacing:.5px}
.company .mark{width:14px;height:14px}
.company .mark.round{border-radius:50%}
.match{position:absolute;right:0;top:10px;width:87px;height:88px;border-left:1px solid #e6e6e6;text-align:center}
.match svg{display:block;margin:0 auto}
.match .pct{position:absolute;left:0;right:0;top:24px;font-size:13px;color:var(--ink)}
.match .label{font-size:11px;color:var(--faint);margin-top:6px}

.backdrop{position:absolute;left:0;top:95px;width:480px;height:756px;background:linear-gradient(160deg,#dcdedd 0%,#cfd2d1 45%,#bfc3c2 100%)}
.sheet{position:absolute;background:var(--card);box-shadow:0 1px 4px rgba(0,0,0,.25)}
.sheet--back2{left:26px;top:126px;width:430px;height:528px;transform:rotate(.6deg)}
.sheet--back1{left:31px;top:131px;width:421px;height:532px;transform:rotate(-.5deg)}
.sheet--front{left:36px;top:136px;width:410px;height:525px}
.sheet .perforation{position:absolute;left:18px;right:18px;top:13px;height:4px;background:radial-gradient(circle,#8a8a8a 1.6px,transparent 2px) 0 0/13.6px 4px repeat-x}
.sheet .job-title{position:absolute;left:0;right:0;top:40px;text-align:center;font-size:21px;color:var(--ink)}
.sheet .company{left:0;right:0;top:89px;justify-content:center}
.duties{position:absolute;left:18px;right:18px;top:139px;list-style:none;border-top:1px solid var(--rule)}
.duties li{height:50.7px;border-bottom:1px solid var(--rule);display:flex;align-items:center;padding-left:39px;position:relative;font-size:17px;color:var(--ink)}
.duties li svg{position:absolute;left:8px;top:18px}

.swipe-bar{position:absolute;left:48px;top:705px;width:386px;height:140px}
.swipe-btn{position:absolute;border-radius:50%;background:radial-gradient(circle at 40% 35%,#fbfaf7,#e5e2dc);box-shadow:0 2px 5px rgba(0,0,0,.18) inset;display:flex;align-items:center;justify-content:center}
</style>
</head>
<body>

<svg class="long-shadows" width="1200" height="1000" aria-hidden="true">
  <polygon points="586,119 1200,733 1200,1000 136,1000 106,970" fill="var(--shadow)" opacity=".55"/>
  <polygon points="1099,119 1200,220 1200,1000 649,1000 619,970" fill="var(--shadow)" opacity=".75"/>
</svg>

<h2 class="screen-title screen-title--shortlist">Shortlist Screen</h2>
<h2 class="screen-title screen-title--detail">Job Description</h2>

<!-- Shortlist -->
<section class="phone phone--shortlist">
  <div class="status-bar">
    <span class="carrier"><span class="signal">●●●○○</span> iLexter
      <svg width="17" height="13" viewBox="0 0 17 13"><path d="M1 5a11 11 0 0 1 15 0M3.5 7.5a7.5 7.5 0 0 1 10 0M6 10a3.5 3.5 0 0 1 5 0" stroke="#fff" stroke-width="1.8" fill="none"/><circle cx="8.5" cy="12" r="1.2" fill="#fff"/></svg></span>
    <span class="time">7:28 PM</span>
    <span class="battery">100%
      <svg width="36" height="15" viewBox="0 0 36 15"><rect x=".75" y=".75" width="31" height="13.5" rx="3" stroke="#fff" stroke-width="1.5" fill="none"/><rect x="3" y="3" width="26.5" height="9" rx="1.5" fill="#fff"/><rect x="33" y="5" width="2.5" height="5" rx="1" fill="#fff"/></svg></span>
  </div>
  <header class="nav-bar">
    <svg width="36" height="28" viewBox="0 0 36 28"><rect y="1" width="36" height="5" fill="#fff"/><rect y="11.5" width="36" height="5" fill="#fff"/><rect y="22" width="36" height="5" fill="#fff"/></svg>
    <h1>Shortlist</h1>
    <svg width="36" height="36" viewBox="0 0 36 36"><g fill="#fff"><circle cx="18" cy="18" r="12"/><g id="teeth"><rect x="15" y="1" width="6" height="8" rx="1"/><rect x="15" y="27" width="6" height="8" rx="1"/><rect x="1" y="15" width="8" height="6" rx="1"/><rect x="27" y="15" width="8" height="6" rx="1"/></g><use href="#teeth" transform="rotate(45 18 18)"/></g><circle cx="18" cy="18" r="5.5" fill="var(--blue)"/></svg>
  </header>

  <div class="job-list">
    <article class="job-card">
      <div class="title">Coordinator Productive &amp; Technique</div>
      <div class="days">8 days left</div>
      <div class="company" style="color:var(--red)"><span class="mark round" style="background:var(--red)"></span>Veltra</div>
      <div class="match"><svg width="64" height="64" viewBox="0 0 64 64"><circle cx="32" cy="32" r="27" stroke="var(--track)" stroke-width="8" fill="none"/><circle cx="32" cy="32" r="27" stroke="var(--ring)" stroke-width="8" fill="none" stroke-dasharray="113.6 170" transform="rotate(-90 32 32)"/></svg><span class="pct">67%</span><div class="label">Matches Skill</div></div>
    </article>
    <article class="job-card">
      <div class="title">Global Acceptance Manager</div>
      <div class="days">7 days left</div>
      <div class="company" style="color:var(--red)"><span class="mark" style="background:var(--red)"></span>Norvik</div>
      <div class="match"><svg width="64" height="64" viewBox="0 0 64 64"><circle cx="32" cy="32" r="27" stroke="var(--track)" stroke-width="8" fill="none"/><circle cx="32" cy="32" r="27" stroke="var(--ring)" stroke-width="8" fill="none" stroke-dasharray="84.8 170" transform="rotate(-90 32 32)"/></svg><span class="pct">50%</span><div class="label">Matches Skill</div></div>
    </article>
    <article class="job-card">
      <div class="title">Financial Reporter</div>
      <div class="days">7 days left</div>
      <div class="company" style="color:var(--navy)"><span class="mark" style="background:var(--navy)"></span>Seaholm</div>
      <div class="match"><svg width="64" height="64" viewBox="0 0 64 64"><circle cx="32" cy="32" r="27" stroke="var(--ring)" stroke-width="8" fill="none"/></svg><span class="pct">100%</span><div class="label">Matches Skill</div></div>
    </article>
    <article class="job-card">
      <div class="title">New Busines Project Manager</div>
      <div class="days">6 days left</div>
      <div class="company" style="color:var(--red)"><span class="mark" style="background:var(--red)"></span>Daxel</div>
      <div class="match"><svg width="64" height="64" viewBox="0 0 64 64"><circle cx="32" cy="32" r="27" stroke="var(--track)" stroke-width="8" fill="none"/><circle cx="32" cy="32" r="27" stroke="var(--ring)" stroke-width="8" fill="none" stroke-dasharray="127.2 170" transform="rotate(-90 32 32)"/></svg><span class="pct">75%</span><div class="label">Matches Skill</div></div>
    </article>
    <article class="job-card">
      <div class="title">SCM Project Manger</div>
      <div class="days">5 days left</div>
      <div class="company" style="color:#1a1a1a"><span class="mark" style="background:var(--red)"></span>Corwell</div>
      <div class="match"><svg width="64" height="64" viewBox="0 0 64 64"><circle cx="32" cy="32" r="27" stroke="var(--track)" stroke-width="8" fill="none"/><circle cx="32" cy="32" r="27" stroke="var(--ring)" stroke-width="8" fill="none" stroke-dasharray="113.6 170" transform="rotate(-90 32 32)"/></svg><span class="pct">67%</span><div class="label">Matches Skill</div></div>
    </article>
    <article class="job-card">
      <div class="title">Financial Reporter</div>
      <div class="days">4 days left</div>
      <div class="company" style="color:var(--red)"><span class="mark round" style="background:var(--red)"></span>Veltra</div>
      <div class="match"><svg width="64" height="64" viewBox="0 0 64 64"><circle cx="32" cy="32" r="27" stroke="var(--ring)" stroke-width="8" fill="none"/></svg><span class="pct">100%</span><div class="label">Matches Skill</div></div>
    </article>
    <article class="job-card">
      <div class="title">Coordinator Productive &amp; Technique</div>
      <div class="days">3 days left</div>
      <div class="match"><svg width="64" height="64" viewBox="0 0 64 64"><circle cx="32" cy="32" r="27" stroke="var(--track)" stroke-width="8" fill="none"/><circle cx="32" cy="32" r="27" stroke="var(--ring)" stroke-width="8" fill="none" stroke-dasharray="113.6 170" transform="rotate(-90 32 32)"/></svg></div>
    </article>
  </div>
</section>

<!-- Job Description -->
<section class="phone phone--detail">
  <div class="status-bar">
    <span class="carrier"><span class="signal">●●●○○</span> iLexter
      <svg width="17" height="13" viewBox="0 0 17 13"><path d="M1 5a11 11 0 0 1 15 0M3.5 7.5a7.5 7.5 0 0 1 10 0M6 10a3.5 3.5 0 0 1 5 0" stroke="#fff" stroke-width="1.8" fill="none"/><circle cx="8.5" cy="12" r="1.2" fill="#fff"/></svg></span>
    <span class="time">7:28 PM</span>
    <span class="battery">100%
      <svg width="36" height="15" viewBox="0 0 36 15"><rect x=".75" y=".75" width="31" height="13.5" rx="3" stroke="#fff" stroke-width="1.5" fill="none"/><rect x="3" y="3" width="26.5" height="9" rx="1.5" fill="#fff"/><rect x="33" y="5" width="2.5" height="5" rx="1" fill="#fff"/></svg></span>
  </div>
  <header class="nav-bar">
    <svg width="36" height="28" viewBox="0 0 36 28"><rect y="1" width="36" height="5" fill="#fff"/><rect y="11.5" width="36" height="5" fill="#fff"/><rect y="22" width="36" height="5" fill="#fff"/></svg>
    <h1>Job Description</h1>
    <svg width="36" height="36" viewBox="0 0 36 36"><g fill="#fff"><circle cx="18" cy="18" r="12"/><g id="teeth2"><rect x="15" y="1" width="6" height="8" rx="1"/><rect x="15" y="27" width="6" height="8" rx="1"/><rect x="1" y="15" width="8" height="6" rx="1"/><rect x="27" y="15" width="8" height="6" rx="1"/></g><use href="#teeth2" transform="rotate(45 18 18)"/></g><circle cx="18" cy="18" r="5.5" fill="var(--blue)"/></svg>
  </header>

  <div class="backdrop" role="img" aria-label="Soft desaturated photo of an office desk with books and handwritten letters"></div>

  <div class="sheet sheet--back2"></div>
  <div class="sheet sheet--back1"></div>
  <article class="sheet sheet--front">
    <div class="perforation"></div>
    <div class="job-title">Global Acceptance Manager</div>
    <div class="company" style="color:var(--red)"><span class="mark" style="background:var(--red)"></span>Norvik</div>
    <ul class="duties">
      <li><svg width="14" height="13" viewBox="0 0 14 13"><path d="M1 7l4 4 8-10" stroke="var(--tick)" stroke-width="2.2" fill="none"/></svg>Lead 20 enthusiastic workers</li>
      <li><svg width="14" height="13" viewBox="0 0 14 13"><path d="M1 7l4 4 8-10" stroke="var(--tick)" stroke-width="2.2" fill="none"/></svg>Coordinate between production</li>
      <li>department and development team</li>
      <li><svg width="14" height="13" viewBox="0 0 14 13"><path d="M1 7l4 4 8-10" stroke="var(--tick)" stroke-width="2.2" fill="none"/></svg>Improve currrent processes</li>
      <li><svg width="14" height="13" viewBox="0 0 14 13"><path d="M1 7l4 4 8-10" stroke="var(--tick)" stroke-width="2.2" fill="none"/></svg>Maintain good relationship with other</li>
      <li>workers</li>
      <li><svg width="14" height="13" viewBox="0 0 14 13"><path d="M1 7l4 4 8-10" stroke="var(--tick)" stroke-width="2.2" fill="none"/></svg>Lots of focus on personal development</li>
    </ul>
  </article>

  <div class="swipe-bar">
    <svg width="386" height="140" viewBox="0 0 386 140" style="position:absolute;left:0;top:0">
      <path d="M50 30 C90 30 110 42 150 34 C175 4 215 4 240 34 C280 42 300 30 336 30 A48 48 0 0 1 336 126 C300 126 280 114 240 122 C215 150 175 150 150 122 C110 114 90 126 50 126 A48 48 0 0 1 50 30Z" fill="#ebe9e4" stroke="#d6d3cd"/>
    </svg>
    <div class="swipe-btn" style="left:13px;top:41px;width:74px;height:74px">
      <svg width="42" height="44" viewBox="0 0 42 44"><g fill="none" stroke="var(--ring)" stroke-width="2.2" stroke-linejoin="round"><rect x="2" y="4" width="9" height="20" rx="1"/><path d="M11 6c5-3 14-3 20-2 4 1 5 4 3 6 3 1 3 5 0 6 3 1 2 5-1 6h-9c1 5 3 12 0 15-2 2-4 1-4-1 0-5-4-10-9-12"/></g></svg>
    </div>
    <div class="swipe-btn" style="left:150px;top:28px;width:86px;height:86px">
      <svg width="64" height="64" viewBox="0 0 64 64"><circle cx="32" cy="32" r="28" stroke="var(--ring)" stroke-width="2.5" fill="none"/><circle cx="32" cy="19" r="3.2" fill="var(--ring)"/><path d="M26 27h8v19h4M26 46h12" stroke="var(--ring)" stroke-width="3" fill="none"/></svg>
    </div>
    <div class="swipe-btn" style="left:299px;top:41px;width:74px;height:74px">
      <svg width="42" height="44" viewBox="0 0 42 44" style="transform:scaleY(-1)"><g fill="none" stroke="var(--ring)" stroke-width="2.2" stroke-linejoin="round"><rect x="2" y="4" width="9" height="20" rx="1"/><path d="M11 6c5-3 14-3 20-2 4 1 5 4 3 6 3 1 3 5 0 6 3 1 2 5-1 6h-9c1 5 3 12 0 15-2 2-4 1-4-1 0-5-4-10-9-12"/></g></svg>
    </div>
  </div>
</section>

</body>
</html>
```